Personal Trainer / Functional Fitness Flyer

We need a flyer for a unique personal training studio / 1 on 1 training.

As far as the images of the tight fascia, previous injuries, etc. I would like to see each image in a box, and possibly black and white with an orange text over it.

Same goes for the QRT logo and images.

Also, fade the pictures of the two trainers in the background where it says 'picture of ross' (MALE TRAINER IN STONEFIELD SHIRT), and picture of 'LENA2 on Right'

anywhere it says' kinetiform fitness" please use logo as best you can.

Thanks .

The image 'lena2' obviously needs some editing.

Target Market(s)

seniors, athletes, functionally fitness minded people

Industry/Entity Type

Fitness

Colors
f37122
fee3d4

Requirements
Must have
• I dont know? basically everything I had in the descritpion
• greyscale some of it.
• just make it look crisp and clean.
Nice to have
• I think use the colors from my logo. just be creative and professional.

```html
<!DOCTYPE html>
<html lang="en">
<head>
<meta charset="utf-8">
<title>Motion Forward Fitness – Flyer</title>
<link href="https://fonts.googleapis.com/css2?family=Oswald:wght@400;500;700&family=Open+Sans:wght@400;600;700&display=swap" rel="stylesheet">
<style>
  :root{
    --orange:#f37122;
    --peach:#fee3d4;
    --dark:#262626;
    --darker:#1c1c1c;
    --green:#8ea55a;
    --grey:#9a9a9a;
    --ink:#222;
    --white:#fff;
  }
  *{box-sizing:border-box;margin:0;padding:0}
  html,body{width:857px;height:1200px;overflow:hidden;background:#fff}
  body{font-family:"Open Sans",Arial,sans-serif;color:var(--ink)}
  .flyer{position:relative;width:857px;height:1200px;background:var(--white);overflow:hidden}
  .hero{position:absolute;left:0;top:0;width:857px;height:560px}
  .side-panel{position:absolute;left:0;top:540px;width:315px;height:660px;background:var(--dark)}

  .badge{position:absolute;left:34px;top:296px;width:244px;height:244px;border-radius:50%;
    background:var(--green);border:7px solid var(--darker);display:flex;flex-direction:column;
    align-items:center;justify-content:center;text-align:center;font-family:"Oswald",sans-serif;
    color:#f4f4ea;font-size:26px;line-height:33px;font-weight:400}
  .badge .brand{color:var(--darker);font-weight:500}

  .tab{position:absolute;height:23px;font-weight:600;font-size:16px;line-height:23px}
  .tab--orange{background:var(--orange);color:var(--white);padding:0 12px 0 20px;border-radius:0 12px 12px 0}
  .tab--green{background:var(--green);color:#20280f;text-align:center;border-radius:12px 0 0 12px}

  .about{position:absolute;left:23px;top:578px;width:282px;color:var(--white);font-size:10px;line-height:15.2px;text-align:justify}
  .audience-intro{position:absolute;left:23px;top:843px;width:282px;color:var(--white);font-size:10px;line-height:14px}
  .audience{position:absolute;top:884px;list-style:none;color:var(--white);font-size:8px;line-height:17.5px;text-transform:uppercase}
  .audience li::before,.creds li::before{content:"✓";color:var(--orange);font-weight:700;margin-right:8px}
  .audience--a{left:23px}.audience--b{left:162px}

  .call{position:absolute;left:23px;top:1022px;font-family:"Oswald",sans-serif;color:var(--white);font-size:18px;font-weight:500}
  .call .phone{color:var(--orange);font-size:31px;margin-left:8px;font-weight:500}

  .trainer-band{position:absolute;left:0;top:1068px;width:380px;height:98px;background:var(--green)}
  .trainer-name{position:absolute;left:23px;top:1074px;font-family:"Oswald",sans-serif;font-weight:700;font-size:15px;color:var(--darker)}
  .trainer-name span{font-family:"Open Sans",sans-serif;font-weight:600;font-size:10px;color:var(--white)}
  .creds{position:absolute;left:23px;top:1096px;list-style:none;font-size:7.8px;line-height:12.5px;color:var(--darker)}
  .trainer-photo{position:absolute;left:360px;top:1000px;width:150px;height:200px;border-radius:70px 70px 0 0;
    background:linear-gradient(180deg,#c99779 0%,#a87258 40%,#1d1d1d 55%,#111 100%)}

  .footer{position:absolute;left:0;top:1166px;width:330px;height:34px;background:var(--darker);color:var(--white);
    font-size:8px;line-height:34px;padding-left:23px}
  .footer .sep{color:var(--orange);margin:0 8px}

  .headline{position:absolute;right:23px;top:498px;text-align:right;font-family:"Oswald",sans-serif;font-weight:700;
    font-size:45px;line-height:55px;color:var(--darker);letter-spacing:-.3px}
  .tagline{position:absolute;right:23px;top:609px;color:var(--orange);font-size:21px;text-align:right}
  .intro{position:absolute;left:470px;right:23px;top:690px;text-align:center;font-size:9.6px;line-height:13.5px;font-weight:700}

  .issues{position:absolute;top:748px;list-style:none;text-align:right;font-size:9px;line-height:21px}
  .issues li::after,.benefits li::after{content:"";display:inline-block;width:5px;height:5px;border-radius:50%;
    background:var(--orange);margin-left:9px;vertical-align:middle}
  .issues .wrap{line-height:11px;padding:5px 0}
  .issues--a{right:354px}.issues--b{right:185px}.issues--c{right:31px}

  .benefits{position:absolute;right:23px;top:913px;list-style:none;text-align:right;font-size:9.4px;line-height:22.4px}
  .benefits b{font-weight:700}

  .partners{position:absolute;right:23px;top:1152px;display:flex;align-items:center;gap:12px;white-space:nowrap}
  .partner-name{font-family:"Open Sans",sans-serif;font-size:10px;font-weight:600;color:var(--darker);letter-spacing:.3px}
  .partner-badge{width:44px;height:14px;background:var(--grey)}
</style>
</head>
<body>
<div class="flyer">

  <svg class="hero" viewBox="0 0 857 560" xmlns="http://www.w3.org/2000/svg">
    <defs>
      <linearGradient id="photoTone" x1="0" y1="0" x2="1" y2="1">
        <stop offset="0" stop-color="#e6e6e4"/>
        <stop offset=".45" stop-color="#b9a99b"/>
        <stop offset=".75" stop-color="#e59a8e"/>
        <stop offset="1" stop-color="#3b3b3d"/>
      </linearGradient>
    </defs>
    <path d="M0 0 H857 V425 C700 455 480 480 335 492 C318 494 315 510 315 530 V560 H0 Z" fill="var(--dark)"/>
    <path d="M0 470 C40 500 80 515 130 522 L0 548 Z" fill="var(--orange)"/>
    <path d="M110 0 C60 170 120 360 300 420 C470 470 690 440 857 380" fill="none" stroke="var(--orange)" stroke-width="22"/>
    <path d="M136 0 C90 160 150 340 316 402 C480 455 690 425 857 362" fill="none" stroke="var(--white)" stroke-width="9"/>
    <g role="img" aria-label="Photo of a trainer guiding a client through a sit-up on a stability ball in the studio">
      <path d="M160 0 C120 150 175 320 330 385 C480 440 690 410 857 345 V0 Z" fill="url(#photoTone)"/>
    </g>
  </svg>

  <div class="side-panel"></div>

  <div class="badge">
    <span>REACH YOUR</span>
    <span>POTENTIAL WITH</span>
    <span class="brand">KINETIFORM</span>
    <span class="brand">FITNESS™</span>
  </div>

  <div class="tab tab--orange" style="left:0;top:548px">About Us</div>
  <p class="about">At Motion Forward Fitness, we take a functional approach to fitness and performance based on enhancing human movement, not just appearance. We are the developers of the Kinetiform™ Fitness approach, a revolutionary system of fitness and movement that utilizes total body training and enhances the nervous system. Most people don't know how good they could feel from moving how they were designed to move. Come and experience freedom from pain, limitations and restrictions and take your body and your life to the next level!</p>

  <div class="tab tab--orange" style="left:0;top:812px">Who's it for?</div>
  <p class="audience-intro">We design custom programs for people of all ages and fitness levels, including:</p>
  <ul class="audience audience--a">
    <li>Athletes</li><li>Yogis</li><li>Pilates</li><li>Elderly</li><li>First time exercisers</li><li>Gym rats</li><li>Bro's</li>
  </ul>
  <ul class="audience audience--b">
    <li>Sedentary</li><li>Youth</li><li>Overweight</li><li>Runners</li><li>HIIT athletes</li><li>Pre &amp; post surgery</li><li>Post-physical therapy</li>
  </ul>

  <p class="call">Call or Text :<span class="phone">555-014-2290</span></p>

  <div class="trainer-band"></div>
  <p class="trainer-name">Ross Harlan <span>( Founder and Owner )</span></p>
  <ul class="creds">
    <li>Deep tissue, integrative bodyworker</li>
    <li>QRT Certified and Functional Movement Specialist</li>
    <li>Co-Developer - Kinetiform™ Fitness System</li>
    <li>Former Division 1 Athlete &amp; Academic All American Nominee</li>
    <li>Certified Holistic Health Counselor</li>
  </ul>
  <div class="trainer-photo" role="img" aria-label="Photo of trainer Ross Harlan in a black studio shirt"></div>

  <p class="footer">Follow us online<span class="sep">•</span>www.motionforwardfitness.com</p>

  <h1 class="headline">MOVE BETTER. FEEL BETTER.<br>FUNCTION BETTER.</h1>
  <p class="tagline">Take your health and performance to the next level.</p>

  <div class="tab tab--green" style="left:534px;top:652px;width:323px">Kinetiform Fitness Training</div>
  <p class="intro">At Motion Forward Fitness, we take a unique, individualized, total body, function based approach to human movement. We start be addressing problems that lead to pain, injury and decreased performance:</p>

  <ul class="issues issues--a">
    <li>Sleep Problems</li><li>Toxicity</li><li>Chronic Stress</li><li>Inflammation</li><li>Tight Fascia</li>
  </ul>
  <ul class="issues issues--b">
    <li>Balance / Stability</li><li>Joint Immobility</li><li>Neurological Timing Problems</li><li>Previous Injuries</li><li>Nutritional Inefficiencies</li>
  </ul>
  <ul class="issues issues--c">
    <li>Postural Issues</li><li>Weak Core Strength</li><li class="wrap">Dysfunctional Movement<br>Patterns</li><li>Muscle Imbalances</li>
  </ul>

  <div class="tab tab--green" style="left:611px;top:873px;width:246px">What you can expect:</div>
  <ul class="benefits">
    <li><b>Higher energy levels</b> from efficient core strength and function</li>
    <li><b>Enhanced movement</b> capabilities to decrease injury risk</li>
    <li><b>Reduced pain</b> from ongoing dysfunctional movement patterns</li>
    <li><b>Increased joint mobility</b> for athletic performance and life</li>
    <li><b>Vast improvement</b> in strength, stamina, power and flexibility</li>
    <li><b>Fat burning</b> though targeted high intensity intervals</li>
    <li><b>Improved health</b> through holistic nutritional guidance</li>
    <li><b>More balance and stability</b> - tighter core, more muscle definition</li>
    <li><b>Faster recovery</b> though hands on, myofascial release therapy</li>
    <li><b>Better brain health</b> through the principles of neuroplasticity</li>
  </ul>

  <div class="partners">
    <span class="partner-name">Motion Forward Fitness</span>
    <span class="partner-badge"></span>
    <span class="partner-name">QRT</span>
  </div>

</div>
</body>
</html>
```